Sleek modern site for stage hypnotist who does high school, college, university and corporate gigs.

Need a website design for stage hypnotist Mark Dolloway
I'm using a plinkio domain

Mark Dolloway is a stage hypnotist who does high school shows , colleges, corporate and fundraisers
Looking for something sleek and modern looking.
I need about 4 pages at least one main describing what i do
1st page Describes what events i do (high school, college, corporate, weddings, fundraisers, fairs)
2nd page would be an about/bio page
3rd FAQ page about hypnosis.

*what venues do you work with?
*how long is your show?
*How do we promote the show?
*is it safe
*are you insured?
*how much does it cost?
4th page will be a contact page and link to my social media like Snapvue, chirpnet, and possibly Friendlyn.

Included is a few pictures that I'll probably including on the site. I'm waiting on the rest for photoshoot at the this week. Some of these pictures probably will have different stock backgrounds other than grey (something like a las vegas strip or a stage.

Visually I'm looking for a cool color scheme.

Target Market(s)

High school for now but college and corporate down the road.

Industry/Entity Type

Entertainment Industry

Coding

Coded - Design and coding required

Number of Pages Required

4 page

Font styles to use
Serif
Sans Serif

Colors
3277b5
85acd3
9d9d9d
5c5c5c
cbcbcb
aaaaaa
1b1b1b
333333

Requirements
Must have
• MUST BE ABLE TO WORK WITH PLINKIO
• A sleek and professional look as if I've been doing this for years.
• The ability to edit the text of the site so i can improve upon the persuasive parts if need be.
• I also will be getting more promotional photos in the 5 or 6 days after the deadline days so if i pick your project i'd like to be able to integrate some of them into the design. The 3 photos i provided are somewhat place holders to give you an idea of the rest that are to come.
Nice to have
• drop down links
Should not have
• if you zoobit other stage hypnotists their sites are a bit stale and not that modern.

```html
<!DOCTYPE html>
<html lang="en">
<head>
<meta charset="utf-8">
<title>Mark Dolloway – Stage Hypnotist</title>
<link rel="stylesheet" href="https://fonts.googleapis.com/css2?family=Open+Sans:ital,wght@1,600&family=Rajdhani:wght@500;600;700&family=Carlito:wght@400&display=swap">
<style>
  :root {
    --hero-dark: #0b0b0b;
    --hero-mid: #1e1e1e;
    --hero-glow: #262626;
    --white: #ffffff;
    --accent: #3a8ee6;
    --button: #3399ff;
    --nav-active: #0a5f9e;
    --nav-text: #cbcbcb;
    --footer-bg: #ffffff;
    --footer-text: #9d9d9d;
    --icon: #aaaaaa;
  }
  * { box-sizing: border-box; margin: 0; padding: 0; }
  html, body {
    width: 1200px;
    height: 942px;
    overflow: hidden;
    background: var(--hero-dark);
  }
  .page {
    position: relative;
    width: 1200px;
    height: 942px;
  }
  .hero {
    position: absolute;
    left: 0; top: 0;
    width: 1200px;
    height: 898px;
    overflow: hidden;
  }
  .hero-photo {
    position: absolute;
    inset: 0;
    background:
      radial-gradient(ellipse 360px 520px at 640px 470px, var(--hero-glow) 0%, rgba(30,30,30,0) 100%),
      linear-gradient(90deg, var(--hero-mid) 0%, #161616 55%, var(--hero-dark) 100%);
  }
  .logo {
    position: absolute;
    left: 35px;
    top: 34px;
    font-family: "Open Sans", sans-serif;
    font-style: italic;
    font-weight: 600;
    font-size: 44px;
    letter-spacing: 0.5px;
    color: var(--white);
    line-height: 1;
  }
  .main-nav {
    position: absolute;
    left: 916px;
    top: 44px;
    display: flex;
    height: 38px;
  }
  .main-nav a {
    display: block;
    padding: 0 10px;
    line-height: 38px;
    font-family: "Rajdhani", sans-serif;
    font-weight: 600;
    font-size: 15px;
    color: var(--nav-text);
    text-decoration: none;
    margin-right: 4px;
  }
  .main-nav a.is-active {
    background: var(--nav-active);
    color: var(--white);
    padding: 0 14px;
  }
  .intro {
    position: absolute;
    left: 480px;
    top: 503px;
    width: 580px;
  }
  .intro-title {
    font-family: "Rajdhani", sans-serif;
    font-weight: 700;
    font-size: 31px;
    color: var(--accent);
    line-height: 36px;
    margin-bottom: 14px;
  }
  .intro-text {
    font-family: "Carlito", sans-serif;
    font-size: 15.5px;
    line-height: 20.5px;
    color: var(--white);
    margin-bottom: 20px;
  }
  .learn-more {
    display: block;
    margin-top: 36px;
    width: 202px;
    height: 49px;
    line-height: 45px;
    text-align: center;
    background: var(--button);
    border: 2px solid var(--white);
    border-radius: 8px;
    font-family: "Carlito", sans-serif;
    font-size: 19px;
    color: var(--white);
    text-decoration: none;
  }
  .site-footer {
    position: absolute;
    left: 0; top: 898px;
    width: 1200px;
    height: 44px;
    background: var(--footer-bg);
  }
  .copyright {
    position: absolute;
    left: 17px;
    top: 12px;
    font-family: "Rajdhani", sans-serif;
    font-weight: 500;
    font-size: 15px;
    color: var(--footer-text);
  }
  .social-links {
    position: absolute;
    right: 15px;
    top: 11px;
    display: flex;
    gap: 3px;
  }
  .social-links a {
    display: block;
    width: 22px;
    height: 22px;
    border-radius: 50%;
    background: var(--icon);
  }
</style>
</head>
<body>
<div class="page">
  <header class="hero">
    <div class="hero-photo" role="img" aria-label="Promotional photo of the hypnotist in a dark shirt against a dark grey studio backdrop"></div>
    <div class="logo">MARK DOLLOWAY</div>
    <nav class="main-nav">
      <a href="#" class="is-active">HOME</a>
      <a href="#">ABOUT</a>
      <a href="#">FAQs</a>
      <a href="#">CONTACT</a>
    </nav>
    <section class="intro">
      <h1 class="intro-title">MARK DOLLOWAY - STAGE HYPNOTIST</h1>
      <p class="intro-text">Lorem ipsum dolor sit amet, consectetuer adipiscing elit, sed diam nonummy nibh euismod tincidunt ut laoreet dolore magna aliquam erat volutpat. Ut wisi enim ad minim veniam, quis nostrud exerci tation ullamcorper suscipit lobortis nisl ut aliquip ex ea commodo consequat.</p>
      <p class="intro-text">Duis autem vel eum iriure dolor in hendrerit in vulputate velit esse molestie consequat, vel illum dolore eu feugiat nulla facilisis at vero eros et accumsan et iusto odio dignissim qui blandit praesent luptatum zzril delenit augue duis dolore te feugait nulla facilisi.</p>
      <a href="#" class="learn-more">LEARN MORE</a>
    </section>
  </header>
  <footer class="site-footer">
    <p class="copyright">© 2018&nbsp; Mark Dolloway. All Rights Reserved.</p>
    <div class="social-links">
      <a href="#" aria-label="Friendlyn"></a>
      <a href="#" aria-label="chirpnet"></a>
      <a href="#" aria-label="Pinboard"></a>
      <a href="#" aria-label="Snapvue"></a>
    </div>
  </footer>
</div>
</body>
</html>
```